Folder, biz cards, stationary, mailing labels, and labels containing my logo
Initiative KORVATH an engineering educational non-profit organization
Cutting-Edge
Marcus Tellfair
Executive Director
mtellfair@initiativekorvath-demo.org
www.initiativekorvath-demo.org
I will need a total of 6 business cards made.
we have a secondary logo that could be placed nicely on the back.
IK Main Logo
secondary logo that can be used on some documents

```html
<!DOCTYPE html>
<html lang="en">
<head>
<meta charset="utf-8">
<title>Initiative KORVATH Stationery Set</title>
<link href="https://fonts.googleapis.com/css2?family=Roboto:wght@400;700&display=swap" rel="stylesheet">
<style>
:root{
  --bg:#3a3d42;
  --paper:#ffffff;
  --ink:#1a2a6a;
  --blue:#1e4fd0;
  --blue-deep:#0b1f6e;
  --navy:#071442;
  --muted:#6a7080;
}
*{box-sizing:border-box;margin:0;padding:0}
html,body{width:1200px;height:331px;overflow:hidden}
body{background:var(--bg);font-family:"Roboto",Arial,sans-serif;position:relative}
.piece{position:absolute;background:var(--paper);overflow:hidden;box-shadow:0 2px 6px rgba(0,0,0,.45)}
.wave{position:absolute;left:0;bottom:0;width:100%}
.brand{display:flex;align-items:center;gap:3px;font-weight:700;color:var(--ink);white-space:nowrap;line-height:1}
.brand .mark{background:var(--blue);flex:none}
.brand.light{color:#fff}
.brand.light .mark{background:#fff}
.tiny{font-size:3.5px;color:var(--muted);line-height:1.4;white-space:nowrap}

.card{width:106px;height:60px;left:19px}
.card-front{top:100px}
.card-front .brand{position:absolute;left:6px;top:8px;font-size:7px}
.card-front .brand .mark{width:7px;height:7px}
.card-contact{top:166px}
.card-contact .who{position:absolute;left:6px;top:8px}
.card-contact .name{font-size:5px;font-weight:700;color:var(--ink)}
.card-back{top:235px;background:linear-gradient(160deg,var(--blue) 0%,var(--blue-deep) 60%,var(--navy) 100%)}
.card-back .brand{position:absolute;left:10px;top:22px;font-size:8px}
.card-back .brand .mark{width:8px;height:8px}

.letter{width:140px;height:280px;top:28px}
.letter-first{left:144px}
.letter-first .brand{position:absolute;left:10px;top:12px;font-size:7px}
.letter-first .brand .mark{width:7px;height:7px}
.letter-first .footer{position:absolute;left:10px;bottom:6px}
.letter-second{left:300px}

.env-back{left:444px;top:53px;width:276px;height:138px}
.env-back .flap{position:absolute;inset:0;width:100%;height:100%}
.env-back .tagline{position:absolute;right:14px;top:18px;width:64px;font-size:4.5px;line-height:1.5;color:var(--muted);white-space:normal}

.env-front{left:440px;top:197px;width:136px;height:86px;background:linear-gradient(180deg,var(--paper) 0 30%,var(--blue) 55%,var(--blue-deep) 100%)}
.env-front .brand{position:absolute;left:6px;top:6px;font-size:5px}
.env-front .brand .mark{width:5px;height:5px}

.label{left:598px;top:233px;width:127px;height:50px}
.label .brand{position:absolute;left:6px;top:7px;font-size:5px}
.label .brand .mark{width:5px;height:5px}

.folder{left:763px;top:24px;width:413px;height:283px;background:var(--navy)}
.folder .cover{position:absolute;left:0;top:0;width:50%;height:100%;background:radial-gradient(ellipse at 40% 35%,#1f52d8 0%,#0c2a9a 45%,var(--navy) 100%)}
.folder .cover .brand{position:absolute;left:40px;top:46px;font-size:17px}
.folder .cover .brand .mark{width:16px;height:16px}
.folder .cover .tagline{position:absolute;left:42px;top:78px;width:110px;font-size:5px;line-height:1.6;color:#cdd8ff}
.folder .cover .web{position:absolute;left:42px;bottom:14px;font-size:4px;color:#9fb2f0}
.folder .inside{position:absolute;left:50%;top:0;width:50%;height:100%;background:linear-gradient(180deg,#0d2a8c 0%,#102fa0 50%,#0a1f72 100%)}
.folder .pocket{position:absolute;left:0;bottom:0;width:100%;height:100%}
</style>
</head>
<body>

<section class="piece card card-front" aria-label="Business card front">
  <div class="brand"><span class="mark"></span>Initiative KORVATH</div>
  <svg class="wave" viewBox="0 0 106 16" height="16" preserveAspectRatio="none"><path d="M0 10 Q40 0 106 6 L106 16 L0 16Z" fill="var(--blue)"/><path d="M0 13 Q50 6 106 10 L106 16 L0 16Z" fill="var(--blue-deep)"/></svg>
</section>

<section class="piece card card-contact" aria-label="Business card contact side">
  <div class="who">
    <p class="name">Marcus Tellfair</p>
    <p class="tiny">Executive Director</p>
    <p class="tiny">mtellfair@initiativekorvath-demo.org</p>
    <p class="tiny">www.initiativekorvath-demo.org</p>
  </div>
  <svg class="wave" viewBox="0 0 106 14" height="14" preserveAspectRatio="none"><path d="M0 9 Q45 0 106 5 L106 14 L0 14Z" fill="var(--blue)"/><path d="M0 12 Q50 5 106 9 L106 14 L0 14Z" fill="var(--blue-deep)"/></svg>
</section>

<section class="piece card card-back" aria-label="Business card back">
  <div class="brand light"><span class="mark"></span>Initiative KORVATH</div>
</section>

<section class="piece letter letter-first" aria-label="Letterhead first page">
  <div class="brand"><span class="mark"></span>Initiative KORVATH</div>
  <svg class="wave" viewBox="0 0 140 30" height="30" preserveAspectRatio="none"><path d="M0 14 Q60 0 140 10 L140 30 L0 30Z" fill="var(--blue)"/><path d="M0 20 Q70 8 140 16 L140 30 L0 30Z" fill="var(--blue-deep)"/></svg>
  <p class="tiny footer" style="color:#dfe6ff">Marcus Tellfair · www.initiativekorvath-demo.org</p>
</section>

<section class="piece letter letter-second" aria-label="Letterhead continuation page">
  <svg class="wave" viewBox="0 0 140 30" height="30" preserveAspectRatio="none"><path d="M0 14 Q60 0 140 10 L140 30 L0 30Z" fill="var(--blue)"/><path d="M0 20 Q70 8 140 16 L140 30 L0 30Z" fill="var(--blue-deep)"/></svg>
</section>

<section class="piece env-back" aria-label="Envelope back">
  <svg class="flap" viewBox="0 0 276 138" preserveAspectRatio="none"><path d="M0 0 L138 62 L276 0" fill="none" stroke="#d6d9e0" stroke-width="1"/><path d="M0 138 L110 72 M276 138 L166 72" stroke="#e6e8ee" stroke-width="1"/></svg>
  <p class="tagline">Engineering education for the next generation of builders</p>
</section>

<section class="piece env-front" aria-label="Envelope front">
  <div class="brand"><span class="mark"></span>Initiative KORVATH</div>
</section>

<section class="piece label" aria-label="Mailing label">
  <div class="brand"><span class="mark"></span>Initiative KORVATH</div>
  <svg class="wave" viewBox="0 0 127 14" height="14" preserveAspectRatio="none"><path d="M0 9 Q55 0 127 5 L127 14 L0 14Z" fill="var(--blue)"/><path d="M0 12 Q60 5 127 9 L127 14 L0 14Z" fill="var(--blue-deep)"/></svg>
</section>

<section class="piece folder" aria-label="Presentation folder">
  <div class="cover">
    <div class="brand light"><span class="mark"></span>Initiative KORVATH</div>
    <p class="tagline">Building skills, sparking curiosity, shaping future engineers</p>
    <p class="web">www.initiativekorvath-demo.org</p>
  </div>
  <div class="inside">
    <svg class="pocket" viewBox="0 0 206 283" preserveAspectRatio="none"><path d="M0 150 Q100 120 206 140 L206 283 L0 283Z" fill="#0a1d6a"/><path d="M0 150 Q100 120 206 140" fill="none" stroke="#3b6cf0" stroke-width="1.2"/></svg>
  </div>
</section>

</body>
</html>
```